Report redesign

We need a designer to redesign the attached report and provide us with a template so we can use it for future reports. We want the redesigned report to look like the one in this link:

http://www3.quellbrix.org/docs/QBX_HVL_MPD_NewModelsAddressingSupplyChainTransportRisk_IndustryAgenda_2012.pdf

Colors
0392cd
3176b5
85acd3
85cae6
33a6d7
0292cd
33b8a4

```html
<!DOCTYPE html>
<html lang="en">
<head>
<meta charset="utf-8">
<title>Report Spread – Page 2</title>
<link href="https://fonts.googleapis.com/css2?family=Arimo:wght@400;700&display=swap" rel="stylesheet">
<style>
  :root {
    --backdrop: #9e9e9e;
    --forest: #2f6e3a;
    --paper: #ffffff;
    --ink: #1c1c1c;
    --muted: #8a8a8a;
    --band-dark: #0d0d0d;
    --band-grey: #7a7a7a;
  }
  * { box-sizing: border-box; margin: 0; padding: 0; }
  html, body { width: 1200px; height: 1120px; overflow: hidden; }
  body {
    background: var(--backdrop);
    font-family: "Arimo", Arial, sans-serif;
    color: var(--ink);
    position: relative;
  }
  .spread {
    position: absolute;
    left: 60px; top: 178px;
    width: 1080px; height: 764px;
    display: flex;
    box-shadow: 0 10px 30px rgba(0,0,0,0.25);
  }
  .page { position: relative; width: 540px; height: 764px; overflow: hidden; }
  .page--cover-inside { background: var(--forest); }
  .page--content { background: var(--paper); }

  .brand {
    position: absolute; right: 36px; top: 36px;
    display: flex; align-items: center; gap: 6px;
    font-size: 17px; font-weight: 400; color: var(--ink);
  }
  .brand__dot { width: 11px; height: 11px; border-radius: 50%; background: var(--forest); }

  .disclaimer { position: absolute; left: 60px; top: 78px; width: 430px; }
  .section-title {
    color: var(--forest); font-weight: 700; font-size: 11px;
    text-transform: uppercase; margin-bottom: 6px;
  }
  .disclaimer__body { font-size: 8.6px; line-height: 1.32; text-align: justify; }

  .accent-block {
    position: absolute; left: 0; top: 218px;
    width: 138px; height: 180px;
    background: var(--forest);
  }

  .authors { position: absolute; left: 172px; top: 240px; }
  .authors__title {
    color: var(--forest); font-weight: 700; font-size: 12px; margin-bottom: 14px;
  }
  .author { font-size: 9.5px; line-height: 1.3; margin-bottom: 10px; }
  .author__name { color: var(--forest); font-weight: 700; }
  .author__email { display: block; }

  .footer-band {
    position: absolute; left: 0; top: 680px;
    width: 330px; height: 42px;
    background: var(--band-dark);
    color: #fff; font-size: 8px; line-height: 1.35;
    display: flex; flex-direction: column; justify-content: center; align-items: flex-end;
    padding-right: 40px;
  }
  .footer-tab {
    position: absolute; left: 330px; top: 698px;
    width: 210px; height: 34px;
    background: var(--band-grey);
  }
  .page-number {
    position: absolute; right: 22px; bottom: 14px;
    font-size: 10px; color: var(--muted);
  }
</style>
</head>
<body>
  <div class="spread">
    <section class="page page--cover-inside" aria-label="Inside cover"></section>

    <section class="page page--content">
      <div class="brand"><span class="brand__dot"></span>Verdanta</div>

      <div class="disclaimer">
        <h2 class="section-title">Legal Disclaimer</h2>
        <p class="disclaimer__body">Verdanta makes no representation or warranty as to the accuracy or completeness of the material herein and shall have and accept no liability for any statements, opinions, information or matters (expressed or implied) arising out of, contained in or derived from this document or any omissions from this document, or any other written or oral communication transmitted or made available to any other party in relation to the subject matter of this document. Any use which a third party makes of the work, or any reliance on or decisions to be made based on it, are the responsibility of such third parties. Decisions made or actions taken as a result of our work shall be the responsibility of the parties directly involved in the decisions or actions.</p>
      </div>

      <div class="accent-block" aria-hidden="true"></div>

      <div class="authors">
        <h3 class="authors__title">Study authors:</h3>
        <p class="author"><span class="author__name">Dorian Halvers</span> – Managing Director<span class="author__email">dorian.halvers@verdanta.com</span></p>
        <p class="author"><span class="author__name">Colin Marsby</span> – Head of Business Development<span class="author__email">colin.marsby@verdanta.com</span></p>
        <p class="author"><span class="author__name">Tomasz Wierzbicki</span> – Manager of Operations and Product Development<span class="author__email">tomasz@verdanta.com</span></p>
        <p class="author"><span class="author__name">Luc-André Perrault</span> – Biomass Consultant and Project Manager<span class="author__email">la@verdanta.com</span></p>
        <p class="author"><span class="author__name">Nathan Brevik</span> – Biomass Consultant and Supply Analyst<span class="author__email">nathan@verdanta.com</span></p>
      </div>

      <div class="footer-band">
        <span>Prepared for Brightmere Specialty Alcohols Inc.</span>
        <span>Confidential © 2015 Verdanta Inc.</span>
      </div>
      <div class="footer-tab" aria-hidden="true"></div>
      <span class="page-number">2</span>
    </section>
  </div>
</body>
</html>
```